Business Card Design Project

Corwen Property Management

Our Business is residential property management, we therefore need a card that displays a professional image, but is clear and concise, and easy to read
Updates

We are committed now guys and girls, loving what we are seeing so far! 

Target Market(s)

Landlords, Rental Property Owners

Industry/Entity Type

Residential

Requirements
Must have
• Dean Fosterly - Principal
Tessa Fosterly - Director (Property Management)

PO Box 718
Holloway SA 5093

Dean: 0419 372 508
Tessa: 0419 613 947

www.corwenpropertymanagement.com.au
admin@corwenpropertymanagement.com.au

Nice to have
• I would like the card to be double sided, white background on the information side and then colour on the reverse, in blue or black and incorporating our logo

```html
<!DOCTYPE html>
<html lang="en">
<head>
<meta charset="utf-8">
<title>Corwen Property Management – Business Cards</title>
<link href="https://fonts.googleapis.com/css2?family=Arimo:wght@400;700&display=swap" rel="stylesheet">
<style>
  :root {
    --stage: #e4e4e2;
    --card-white: #ffffff;
    --card-black: #1c1a1a;
    --brand-blue: #2f7fc1;
    --brand-blue-deep: #1b5fa3;
    --ink-grey: #3a3a3a;
    --ink-dark: #111111;
    --ink-light: #ffffff;
  }
  * { box-sizing: border-box; margin: 0; padding: 0; }
  html, body { width: 1200px; height: 951px; overflow: hidden; }
  body {
    background: var(--stage);
    font-family: "Arimo", Arial, sans-serif;
    position: relative;
  }
  .card {
    position: absolute;
    width: 580px;
    height: 340px;
    border-radius: 22px;
    overflow: hidden;
    box-shadow: 0 10px 28px rgba(0,0,0,.25);
  }
  .brand-square { background: var(--brand-blue); flex: none; }
  .brand-name { font-weight: 700; line-height: 1; display: flex; flex-direction: column; }
  .brand-name__main { display: block; }
  .brand-name__sub { display: block; margin-top: 6px; }

  /* front */
  .card--front { left: 90px; top: 90px; background: var(--card-white); }
  .front-brand {
    position: absolute; left: 0; right: 0; top: 112px;
    display: flex; align-items: center; justify-content: center; gap: 16px;
  }
  .front-brand .brand-square { width: 78px; height: 60px; }
  .front-brand .brand-name { color: var(--ink-grey); }
  .front-brand .brand-name__main { font-size: 54px; }
  .front-brand .brand-name__sub { font-size: 17px; }
  .front-web {
    position: absolute; left: 0; right: 0; top: 236px;
    text-align: center; font-size: 15px; color: var(--ink-dark);
  }

  /* back */
  .card--back { left: 530px; top: 480px; background: var(--card-black); color: var(--ink-light); }
  .back-swoosh { position: absolute; inset: 0; width: 100%; height: 100%; }
  .back-brand {
    position: absolute; left: 42px; top: 62px;
    display: flex; align-items: center; gap: 12px;
  }
  .back-brand .brand-square { width: 56px; height: 44px; }
  .back-brand .brand-name { color: var(--ink-light); }
  .back-brand .brand-name__main { font-size: 42px; }
  .back-brand .brand-name__sub { font-size: 13px; margin-top: 4px; }
  .people { position: absolute; left: 42px; top: 192px; }
  .person__name { color: var(--brand-blue); font-size: 18px; line-height: 1.1; }
  .person__role { font-size: 13px; line-height: 1.3; margin-bottom: 6px; }
  .contacts { position: absolute; left: 252px; top: 186px; list-style: none; font-size: 13px; }
  .contacts li { display: flex; align-items: flex-start; gap: 9px; line-height: 1.35; margin-bottom: 3px; }
  .contacts svg { width: 13px; height: 13px; flex: none; margin-top: 2px; }
  .contacts .web-accent { color: var(--brand-blue); }
</style>
</head>
<body>

<section class="card card--front" aria-label="Card front">
  <div class="front-brand">
    <span class="brand-square"></span>
    <span class="brand-name">
      <span class="brand-name__main">Corwen</span>
      <span class="brand-name__sub">Property Management</span>
    </span>
  </div>
  <p class="front-web">www.corwenpropertymanagement.com.au</p>
</section>

<section class="card card--back" aria-label="Card back">
  <svg class="back-swoosh" viewBox="0 0 580 340" preserveAspectRatio="none" aria-hidden="true">
    <path d="M390 0 C480 35 545 110 580 190 L580 0 Z" fill="var(--brand-blue-deep)"/>
    <path d="M425 0 C500 35 555 100 580 160 L580 0 Z" fill="var(--brand-blue)"/>
    <path d="M365 0 C460 30 535 105 580 215" fill="none" stroke="#fff" stroke-width="6"/>
    <path d="M340 0 C445 28 525 115 580 245" fill="none" stroke="#fff" stroke-width="3"/>
  </svg>

  <div class="back-brand">
    <span class="brand-square"></span>
    <span class="brand-name">
      <span class="brand-name__main">Corwen</span>
      <span class="brand-name__sub">Property Management</span>
    </span>
  </div>

  <div class="people">
    <p class="person__name">Dean Fosterly</p>
    <p class="person__role">Principal</p>
    <p class="person__name">Tessa Fosterly</p>
    <p class="person__role">Director<br>(Property Management)</p>
  </div>

  <ul class="contacts">
    <li>
      <svg viewBox="0 0 14 14"><path d="M7 1 L13 7 H11 V13 H8 V9 H6 V13 H3 V7 H1 Z" fill="#fff"/></svg>
      <span>PO Box 718<br>Holloway SA 5093</span>
    </li>
    <li>
      <svg viewBox="0 0 14 14"><path d="M4 1 L6 4 L5 6 C6 8 7 9 8 9 L10 8 L13 10 L11 13 C6 13 1 8 1 3 Z" fill="#fff"/></svg>
      <span>Dean: 0419 372 508</span>
    </li>
    <li>
      <svg viewBox="0 0 14 14"><path d="M4 1 L6 4 L5 6 C6 8 7 9 8 9 L10 8 L13 10 L11 13 C6 13 1 8 1 3 Z" fill="#fff"/></svg>
      <span>Tessa: 0419 613 947</span>
    </li>
    <li>
      <svg viewBox="0 0 14 14"><rect x="1" y="3" width="12" height="8" fill="#fff"/><path d="M1 3 L7 8 L13 3" fill="none" stroke="#1c1a1a" stroke-width="1.2"/></svg>
      <span>admin@corwenpropertymanagement.com.au</span>
    </li>
    <li>
      <svg viewBox="0 0 14 14"><circle cx="7" cy="7" r="6" fill="#fff"/></svg>
      <span>www.<span class="web-accent">corwenpropertymanagement</span>.com.au</span>
    </li>
  </ul>
</section>

</body>
</html>
```